Kneadwell Bodycare Studio

We are a Massage Therapy business based in Invercargill, New Zealand. We specialise in Sports and deep tissue massage but also provide relaxation and aromatherapy massage. We would like to see designs that use the the logo.
The final design should promote health and fitness.
Updates

Hi I am getting feedback that my business card picture is poor quality. I got this picture from brightpress under massage. So if you google this image a better quality picture should come up,. If not hope to upload a better image by tomorow, thanks.

Target Market(s)

Sports, people with pain and injuries

Industry/Entity Type

Massage

Requirements
Must have
• Logo, muscle body that is used on the business card, also a poster that matches my business card
Nice to have
• Picture of muscle man, shown on my business card
Should not have
• Not a picture of a real person

```html
<!DOCTYPE html>
<html lang="en">
<head>
<meta charset="utf-8">
<title>Kneadwell Bodycare Studio – Poster</title>
<link rel="stylesheet" href="https://fonts.googleapis.com/css2?family=Roboto:wght@300;400;500&display=swap">
<style>
  :root {
    --backdrop: #ecebe8;
    --paper: #ffffff;
    --sky-top: #d3e9f3;
    --sky-mid: #eef6fa;
    --cyan: #1fb6d9;
    --aqua: #74cfdc;
    --aqua-soft: #bfe6ee;
    --pink: #e4679f;
    --ink: #555a5e;
    --rule: #b5b8ba;
    --water: #dbe7ee;
  }
  html, body {
    margin: 0;
    width: 1200px;
    height: 1000px;
    overflow: hidden;
    background: var(--backdrop);
    font-family: "Roboto", Arial, sans-serif;
  }
  .canvas { position: relative; width: 1200px; height: 1000px; }
  .poster {
    position: absolute;
    left: 270px; top: 33px;
    width: 660px; height: 932px;
    overflow: hidden;
    background: linear-gradient(180deg, var(--sky-top) 0%, var(--sky-mid) 35%, var(--paper) 55%, var(--paper) 82%, var(--water) 100%);
  }
  .anatomy-figure {
    position: absolute; left: 0; top: 0;
    width: 290px; height: 345px;
    background: radial-gradient(ellipse at 35% 40%, #b9bbbd 0%, #a4a7aa 45%, rgba(210,215,220,0) 80%);
  }
  .headline { position: absolute; left: 326px; top: 52px; color: var(--pink); }
  .headline .lead {
    font-weight: 300; font-size: 24px; color: var(--ink); letter-spacing: 0.5px;
    position: absolute; left: 0; top: 22px; white-space: nowrap;
  }
  .headline .pain {
    font-weight: 400; font-size: 66px; letter-spacing: -2px;
    position: absolute; left: -2px; top: 34px; white-space: nowrap;
  }
  .headline .mark {
    font-weight: 300; font-size: 120px;
    position: absolute; left: 140px; top: -12px;
  }
  .studio-title {
    position: absolute; left: 322px; top: 168px; margin: 0;
    font-weight: 300; font-size: 62px; line-height: 61px;
    color: var(--cyan); letter-spacing: -0.5px;
  }
  .wave { position: absolute; left: 0; top: 320px; width: 660px; height: 170px; }
  .services {
    position: absolute; left: 40px; top: 476px; margin: 0; padding: 0; list-style: none;
    font-weight: 300; font-size: 22px; line-height: 30.5px; color: var(--ink);
  }
  .services li::before {
    content: ""; display: inline-block; width: 8px; height: 8px; border-radius: 50%;
    background: var(--cyan); margin-right: 8px; vertical-align: 3px;
  }
  .booking {
    position: absolute; left: 269px; top: 480px; height: 142px;
    border-left: 1px solid #9a9ea1; padding-left: 12px;
    font-weight: 300; font-size: 17px; line-height: 22.5px; color: var(--ink);
  }
  .booking strong { color: var(--cyan); font-weight: 500; font-size: 18px; }
  .booking .prices-title { color: var(--cyan); font-size: 19px; font-weight: 400; margin-top: 8px; }
  .divider {
    position: absolute; left: 40px; top: 643px; width: 330px;
    border-top: 1px dotted var(--rule);
  }
  .contact { position: absolute; left: 38px; top: 660px; color: var(--ink); }
  .contact .name {
    font-weight: 300; font-size: 24px; color: var(--cyan); white-space: nowrap;
    display: flex; align-items: center; gap: 10px;
  }
  .contact .name .dot { width: 30px; height: 30px; border-radius: 50%; background: var(--cyan); }
  .contact .details { font-weight: 300; font-size: 21px; line-height: 29px; margin-top: 4px; }
  .social {
    position: absolute; left: 40px; top: 818px;
    font-size: 21px; font-weight: 300; color: var(--ink); white-space: nowrap;
  }
</style>
</head>
<body>
<div class="canvas">
  <section class="poster">
    <div class="anatomy-figure" role="img" aria-label="Grey anatomical illustration of a muscular back and arm with blue highlights at the shoulder and elbow"></div>

    <div class="headline">
      <span class="lead">ARE YOU IN</span>
      <span class="pain">PAIN</span>
      <span class="mark">?</span>
    </div>

    <h1 class="studio-title">Kneadwell<br>Bodycare<br>Studio</h1>

    <svg class="wave" viewBox="0 0 660 170" aria-hidden="true">
      <path d="M0 90 C120 20 260 30 360 100 C430 150 520 160 660 95 L660 110 C520 175 420 165 340 115 C250 55 120 45 0 110 Z" fill="var(--aqua)"/>
      <path d="M0 80 C90 50 170 60 240 90 C170 70 90 68 0 96 Z" fill="var(--aqua-soft)"/>
      <path d="M330 95 C420 140 520 140 660 80 L660 86 C520 150 420 150 330 95 Z" fill="var(--aqua-soft)"/>
    </svg>

    <ul class="services">
      <li>Deep Tissue</li>
      <li>Sports Massage</li>
      <li>Remedial Massage</li>
      <li>Relaxation</li>
      <li>Aromatherapy</li>
    </ul>

    <div class="booking">
      <div>Book today</div>
      <div>Call <strong>0275550142</strong></div>
      <div class="prices-title">Prices</div>
      <div>30 minutes: <strong>$40</strong></div>
      <div>60 minutes: <strong>$60</strong></div>
      <div>90 minutes: <strong>$80</strong></div>
    </div>

    <div class="divider"></div>

    <div class="contact">
      <div class="name">Kneadwell Bodycare Studio <span class="dot"></span></div>
      <div class="details">
        Maren Tolley, Bachelor of<br>
        Therapeiutic &amp; Sports Massage<br>
        18 Ferncliff St, Invercargill<br>
        www.kneadwellstudio.co.nz
      </div>
    </div>

    <div class="social">Follow the studio on Pagebook</div>
  </section>
</div>
</body>
</html>
```